Resume for higher management position in a mechanical/consultant industries application*

I would like to use this resume for getting a higher position interview possibilities. My skills are multi-cultural negotiation, mechanical industry sales, outsourcing to Asia, ability to manage the agent/reseller system, well team player. multi-language Chinese/English/German specialized. Please make the design, professional, comfortable to read atmosphere.

Target Market(s)

management position, sales related

Font styles to use
Serif
Sans Serif

```html
<!DOCTYPE html>
<html lang="en">
<head>
<meta charset="utf-8">
<title>Lin-Wei Tsao – Resume and Cover</title>
<link rel="stylesheet" href="https://fonts.googleapis.com/css2?family=Mulish:wght@400;600;700;800&display=swap">
<style>
  :root {
    --stage: #2f4049;
    --paper: #ffffff;
    --navy-top: #16294a;
    --navy-deep: #101a27;
    --cover-top: #1c2e48;
    --cover-bottom: #0f1925;
    --ink: #111111;
    --text: #222222;
    --rule: #cfcfcf;
    --dot-off: #d2d2d2;
    --avatar: #8a8a8a;
    --avatar-ring: #ffffff;
    --light: #ffffff;
  }
  * { box-sizing: border-box; margin: 0; padding: 0; }
  html, body { width: 1200px; height: 720px; overflow: hidden; background: var(--stage); }
  body { position: relative; font-family: "Mulish", sans-serif; color: var(--text); }
  .at { position: absolute; }

  /* ---------- resume sheet ---------- */
  .resume { left: 167px; top: 66px; width: 410px; height: 587px; background: var(--paper); overflow: hidden; }
  .resume-header { left: 0; top: 0; width: 410px; height: 79px; background: linear-gradient(90deg, var(--navy-top), var(--navy-deep)); }
  .avatar { border-radius: 50%; background: radial-gradient(circle at 50% 40%, #9a9a9a, var(--avatar)); border: 2px solid var(--avatar-ring); }
  .resume-header .avatar { left: 35px; top: 12px; width: 56px; height: 56px; }
  .resume-name { left: 106px; top: 22px; font-size: 15.5px; font-weight: 700; color: var(--light); letter-spacing: .2px; }
  .resume-role { left: 109px; top: 41px; font-size: 10.5px; font-weight: 400; color: var(--light); }

  .timeline { width: 1px; background: var(--rule); top: 117px; height: 430px; }
  .timeline.left { left: 36px; }
  .timeline.right { left: 248px; }

  .section-icon { width: 13px; height: 13px; margin: -6.5px 0 0 -6.5px; }
  .section-title { font-size: 8.6px; font-weight: 700; color: var(--ink); transform: translateY(-50%); white-space: nowrap; }

  .info { left: 49px; top: 143px; width: 170px; font-size: 5.3px; line-height: 8.8px; }
  .info dt { font-weight: 700; color: var(--ink); padding-left: 1px; }
  .info dd { color: var(--text); }

  .entry-dot { width: 3.2px; height: 3.2px; border-radius: 50%; background: var(--ink); margin: -1.6px 0 0 -1.6px; left: 36px; }
  .entry-title { left: 49px; width: 180px; font-size: 7.2px; line-height: 8.8px; font-weight: 700; color: var(--ink); }
  .entry-body { left: 50px; width: 172px; font-size: 5.2px; line-height: 7.35px; list-style: none; }
  .entry-body li { position: relative; padding-left: 5px; }
  .entry-body li::before { content: "•"; position: absolute; left: 0; top: 0; }
  .entry-body li.plain::before { content: ""; }
  .entry-body li + li { margin-top: 3.5px; }

  .lang-name { left: 261px; font-size: 5.3px; }
  .lang-dots { left: 333px; width: 32px; height: 5px; display: flex; justify-content: space-between; }
  .lang-dots span { width: 5px; height: 5px; border-radius: 50%; background: var(--ink); }
  .lang-dots span.off { background: var(--dot-off); }
  .lang-level { right: 46px; font-size: 5.3px; text-align: right; }

  .summary { left: 261px; width: 130px; font-size: 5.2px; line-height: 7.35px; }

  /* ---------- cover sheet ---------- */
  .cover { left: 623px; top: 66px; width: 410px; height: 587px; background: linear-gradient(180deg, var(--cover-top), var(--cover-bottom)); }
  .cover .avatar { left: 141px; top: 186px; width: 124px; height: 124px; border-width: 3px; }
  .cover-name { left: 0; width: 422px; top: 336px; text-align: center; font-size: 29px; font-weight: 800; color: var(--light); letter-spacing: .3px; }
  .cover-role { left: 0; width: 422px; top: 373px; text-align: center; font-size: 20px; font-weight: 400; color: var(--light); }
</style>
</head>
<body>

<section class="resume at" aria-label="Resume">
  <header class="resume-header at">
    <div class="avatar at" role="img" aria-label="Portrait photo placeholder"></div>
    <h1 class="resume-name at">Lin-Wei Tsao</h1>
    <p class="resume-role at">Sales manager Asia</p>
  </header>

  <div class="timeline left at"></div>
  <div class="timeline right at"></div>

  <!-- Personal information -->
  <svg class="section-icon at" style="left:36px;top:117px" viewBox="0 0 20 20" aria-hidden="true">
    <circle cx="10" cy="10" r="10" fill="#111"/>
    <circle cx="10" cy="8" r="3" fill="none" stroke="#fff" stroke-width="1.4"/>
    <path d="M4.8 15.5c1-2.8 3-3.8 5.2-3.8s4.2 1 5.2 3.8" fill="none" stroke="#fff" stroke-width="1.4"/>
  </svg>
  <h2 class="section-title at" style="left:49px;top:117px">Personal Information</h2>
  <dl class="info at" style="top:127px">
    <dt>Home Address</dt><dd>+xxxxxx</dd>
    <dt>Nationality</dt><dd>Taiwanese</dd>
    <dt>Contact Number</dt><dd>+xxxxxx</dd>
    <dt>E-mail Address</dt><dd>xxxxxx@mailbox.com</dd>
    <dt>ProfileNet:</dt><dd>https://www.profilenet.com/in/xxxx</dd>
  </dl>

  <!-- Work experience -->
  <svg class="section-icon at" style="left:36px;top:230px" viewBox="0 0 20 20" aria-hidden="true">
    <circle cx="10" cy="10" r="10" fill="#111"/>
    <rect x="4.5" y="7" width="11" height="8" rx="1" fill="none" stroke="#fff" stroke-width="1.3"/>
    <path d="M8 7V5.5h4V7M4.5 10.5h11" fill="none" stroke="#fff" stroke-width="1.3"/>
  </svg>
  <h2 class="section-title at" style="left:49px;top:230px">Work Experience</h2>

  <span class="entry-dot at" style="top:245px"></span>
  <h3 class="entry-title at" style="top:240px">Sales Manager Asiaxxxxxxxxx 2018-now</h3>
  <ul class="entry-body at" style="top:251px">
    <li>Currently, leading 3 major dealers in Taiwan, Mainland China, South Korea and Japan with more than 20 salesmen team. Kornhaus provides rotary tables, trunnions and 2 axis rotary tilt units shall have the best possible technical characteristics in the smallest possible space, is the principle model for our dividing heads -engineering -manufacturing -and assembly.</li>
  </ul>

  <span class="entry-dot at" style="top:307px"></span>
  <h3 class="entry-title at" style="top:302px">Director of Manufacturing, Brightmill Precision Machinery Company 2012-2017</h3>
  <ul class="entry-body at" style="top:323px">
    <li>Using CNC turn/mill machine to manufacture any mechanical components as customers want. Also providing great total solutions for our clients.</li>
    <li class="plain">Photos shown in my ProfileNet are my products which are made by CNC turn-milling dual spindles machines(trophy is programmed by CAM).</li>
  </ul>

  <span class="entry-dot at" style="top:381px"></span>
  <h3 class="entry-title at" style="top:376px">Marketing Analyst, Northgate Import Mannheim Germany, 2012 Apr- 2012 Nov</h3>
  <ul class="entry-body at" style="top:395px">
    <li>Help Northgate Import to build their sales/marketing strategy for the new launched product “Slickguard” in central Europe.</li>
  </ul>

  <span class="entry-dot at" style="top:421px"></span>
  <h3 class="entry-title at" style="top:416px">External consultant, Calvera Group Bergamo Italty, 2011 Oct-2012 Mar</h3>
  <ul class="entry-body at" style="top:435px">
    <li>To improve the Vista solution (ERP system) of Calvera Group with re-organized procurement process and new standardized KPIs.</li>
  </ul>

  <!-- Education -->
  <svg class="section-icon at" style="left:36px;top:462px" viewBox="0 0 20 20" aria-hidden="true">
    <circle cx="10" cy="10" r="10" fill="#111"/>
    <path d="M3.5 8.5 10 5.5l6.5 3-6.5 3z" fill="none" stroke="#fff" stroke-width="1.2"/>
    <path d="M6.5 10v3c1 1 2.2 1.4 3.5 1.4s2.5-.4 3.5-1.4v-3" fill="none" stroke="#fff" stroke-width="1.2"/>
  </svg>
  <h2 class="section-title at" style="left:49px;top:462px">Educational Attainment</h2>

  <span class="entry-dot at" style="top:477px"></span>
  <h3 class="entry-title at" style="top:472px">MBA</h3>
  <ul class="entry-body at" style="top:484px">
    <li>Accademia Tecnica Milano Italy 2011-2012</li>
  </ul>

  <span class="entry-dot at" style="top:502px"></span>
  <h3 class="entry-title at" style="top:497px">Bachelor of Chemical Engineering</h3>
  <ul class="entry-body at" style="top:509px">
    <li>Ming-Hsin Lakeside University 2005-200</li>
  </ul>

  <!-- Languages -->
  <svg class="section-icon at" style="left:248px;top:117px" viewBox="0 0 20 20" aria-hidden="true">
    <circle cx="10" cy="10" r="10" fill="#111"/>
    <path d="M6.5 15V5M6.5 5.5h7l-1.5 2.5 1.5 2.5h-7" fill="none" stroke="#fff" stroke-width="1.2"/>
  </svg>
  <h2 class="section-title at" style="left:260px;top:119px">Languages</h2>

  <span class="lang-name at" style="top:127px">Chinese</span>
  <div class="lang-dots at" style="top:137px"><span></span><span></span><span></span><span></span><span></span></div>
  <span class="lang-level at" style="top:146px">Native</span>

  <span class="lang-name at" style="top:158px">English</span>
  <div class="lang-dots at" style="top:168px"><span></span><span></span><span></span><span class="off"></span><span></span></div>
  <span class="lang-level at" style="top:176px">Avanced</span>

  <span class="lang-name at" style="top:189px">German</span>
  <div class="lang-dots at" style="top:199px"><span></span><span></span><span></span><span class="off"></span><span class="off"></span></div>
  <span class="lang-level at" style="top:207px">Avanced</span>

  <!-- Summary -->
  <svg class="section-icon at" style="left:248px;top:229px" viewBox="0 0 20 20" aria-hidden="true">
    <circle cx="10" cy="10" r="10" fill="#111"/>
    <circle cx="10" cy="10" r="4.5" fill="none" stroke="#fff" stroke-width="1.2"/>
    <circle cx="10" cy="10" r="1.4" fill="#fff"/>
    <path d="M10 3v3.5M10 13.5V17M3 10h3.5M13.5 10H17" stroke="#fff" stroke-width="1.2"/>
  </svg>
  <h2 class="section-title at" style="left:260px;top:229px">Summary</h2>

  <p class="summary at" style="top:239px">Mandarin Chinese/ German/ English speaker, real machining experiences, OEM skills, trade skill, global sourcing</p>
  <p class="summary at" style="top:276px">Currently, I am a “Sales manager Asia” of a top German rotary table company. I am in charge of four countries Japan, China, South Korea and Taiwan with 3 agents, more than 20 salemen team.</p>
  <p class="summary at" style="top:321px">As a director of manufacuting, I have more than 5 years professional experiences in manufacturing metal components by different CNC-machines. I am capable of coding CNC G, M-code, designing the working path of different parts and managing the whole process.</p>
  <p class="summary at" style="top:372px">I have well-understanding of mechanical outsourcing ecosystem in Taiwan. With deep knowledge of outsourcing metal components to different suppliers in Taiwan.</p>
  <p class="summary at" style="top:409px">Familiar with coordinating with different industrial processes in order to build the final products. (Black oxidizing, Different anodizing, Chemical polishing, Manganese phosphate coating, Heat treatment, and Different grinding methods) Especially love to build prototype in order to get a high profitable potential products. (from zero to one).</p>
</section>

<section class="cover at" aria-label="Resume cover">
  <div class="avatar at" role="img" aria-label="Portrait photo placeholder"></div>
  <h1 class="cover-name at">Lin-Wei Tsao</h1>
  <p class="cover-role at">Sales manager Asia</p>
</section>

</body>
</html>
```